Birchwood Clover Business Cards

I need a business card with my logo, number, Facebook account, and some information about what I am selling. Green card with logo on the front. 555-218-3946 phone number, @birchwoodclover Facebook, •Orchardgrass Hay •Alfalfa Hay •Mixed Grass Hay , and “Premium Quality Hay” all written on the back.

Target Market(s)

Hay

Contact Information for Business Card

Phone number, Facebook, different types of hay.

Colors
00AB8E
00BBA5
67D7C9
C6EFE9
E9F9F6

```html
<!DOCTYPE html>
<html lang="en">
<head>
<meta charset="utf-8">
<title>Birchwood Clover Business Cards</title>
<link href="https://fonts.googleapis.com/css2?family=Roboto:wght@400;500;700&family=Kaushan+Script&display=swap" rel="stylesheet">
<style>
  :root {
    --page: #e6e7e6;
    --card-dark: #161616;
    --card-light: #f7f7f5;
    --green: #1fa84b;
    --ink: #111111;
    --white: #ffffff;
  }
  * { box-sizing: border-box; margin: 0; padding: 0; }
  html, body {
    width: 1200px;
    height: 874px;
    overflow: hidden;
    background: var(--page);
    font-family: "Roboto", Arial, sans-serif;
  }
  .sheet {
    position: relative;
    width: 1200px;
    height: 874px;
  }
  .card {
    position: absolute;
    width: 600px;
    height: 343px;
    border-radius: 22px;
    overflow: hidden;
    box-shadow: 0 10px 26px rgba(0,0,0,0.22);
  }

  /* Back card */
  .card-back {
    left: 520px;
    top: 60px;
    background: var(--card-dark);
    color: var(--white);
  }
  .back-brand {
    position: absolute;
    left: 0;
    right: 0;
    top: 112px;
    display: flex;
    align-items: center;
    justify-content: center;
    gap: 16px;
  }
  .brand-dot {
    width: 44px;
    height: 44px;
    border-radius: 50%;
    background: var(--green);
  }
  .back-brand .brand-name {
    font-size: 34px;
    font-weight: 500;
    color: var(--white);
  }
  .product-list {
    position: absolute;
    left: 0;
    right: 0;
    top: 236px;
    text-align: center;
    font-size: 18px;
    line-height: 1.25;
  }
  .product-list .rule {
    display: block;
    width: 330px;
    height: 2px;
    margin: 4px auto 3px;
    background: var(--green);
  }

  /* Front card */
  .card-front {
    left: 80px;
    top: 470px;
    background: var(--card-light);
    color: var(--ink);
  }
  .front-mark {
    position: absolute;
    left: 70px;
    top: 70px;
    width: 120px;
    height: 120px;
    border-radius: 50%;
    background: var(--green);
  }
  .front-name {
    position: absolute;
    left: 212px;
    top: 78px;
    font-family: "Kaushan Script", cursive;
    font-size: 44px;
    color: var(--ink);
  }
  .front-phone {
    position: absolute;
    left: 212px;
    top: 148px;
    font-size: 44px;
    font-weight: 700;
    letter-spacing: 0.5px;
  }
  .front-band {
    position: absolute;
    left: 0;
    right: 0;
    bottom: 0;
    height: 86px;
    background: var(--green);
    border-top: 6px solid var(--ink);
    box-shadow: 0 -4px 0 var(--card-light), 0 -6px 0 var(--ink);
    display: flex;
    align-items: center;
    justify-content: center;
    gap: 10px;
    color: var(--white);
    font-size: 21px;
    font-weight: 500;
  }
  .social-dot {
    width: 22px;
    height: 22px;
    border-radius: 50%;
    background: var(--white);
  }
</style>
</head>
<body>
  <main class="sheet">
    <section class="card card-back" aria-label="Card back">
      <div class="back-brand">
        <span class="brand-dot"></span>
        <span class="brand-name">Birchwood Clover</span>
      </div>
      <p class="product-list">
        Orchardgrass Hay • Alfalfa Hay
        <span class="rule"></span>
        Mixed Grass Hay, &amp; Premium Quality Hay
      </p>
    </section>

    <section class="card card-front" aria-label="Card front">
      <span class="front-mark"></span>
      <h1 class="front-name">Birchwood Clover</h1>
      <p class="front-phone">555-218-3946</p>
      <footer class="front-band">
        <span class="social-dot"></span>
        <span class="social-handle">@birchwoodclover</span>
      </footer>
    </section>
  </main>
</body>
</html>
```